Business card design for sports medicine and athlete care clinic.

We need a bold, solid business card design for our practitioners to stand out. We treat overuse & sports-related injuries and provide post-operative rehabilitation. Our specialisations include chronic conditions, men’s health, nutrition & musculoskeletal disorders (MSDs). All brand collateral in terms of fonts, logo and colour palette to be provided.

Target Market(s)

Athletes (professional and amateur), sportspeople, predominantly male

Industry/Entity Type

Health And Wellness

Contact Information for Business Card

The front of the card should be white with dark blue text the back dark blue with white text. The logo should be top-left. The business name should be horizontal and right of the logo. The tagline should be directly below centred on the back of the card (see top-banner.png and bottom-banner.png)

Font styles to use
Sans Serif

Colors
0355a3
0293ce
3176b5
ffffff
85acd3

Requirements
Nice to have
• Diagonal and/or horizontal line elements between logo and practitioner details and/or bottom corner of card (see slide.png and tag-bg.png).

```html
<!DOCTYPE html>
<html lang="en">
<head>
<meta charset="utf-8">
<title>The Runner's Haven – Business Card</title>
<link rel="stylesheet" href="https://fonts.googleapis.com/css2?family=Montserrat:wght@500;700;800&family=Arimo:wght@400&display=swap">
<style>
  :root {
    --backdrop: #1f1f21;
    --card-white: #f4f5f6;
    --navy: #0b2166;
    --ink: #0d2a6e;
    --accent: #0293ce;
    --brand-blue: #0355a3;
    --text-dark: #1a1a1a;
    --divider: #d3d6da;
    --white: #ffffff;
  }
  * { box-sizing: border-box; margin: 0; padding: 0; }
  html, body { width: 1200px; height: 900px; overflow: hidden; }
  body {
    background: var(--backdrop);
    font-family: "Arimo", Arial, sans-serif;
    position: relative;
  }
  .card {
    position: absolute;
    width: 540px;
    height: 320px;
    border-radius: 26px;
    top: 290px;
    overflow: hidden;
  }
  .card--front { left: 40px; background: var(--card-white); }
  .card--back { left: 620px; background: var(--navy); color: var(--white); }

  /* shared brand lockup */
  .brand {
    position: absolute;
    display: flex;
    align-items: center;
    gap: 10px;
  }
  .brand__dot {
    width: 30px; height: 30px; border-radius: 50%;
    background: var(--accent);
    flex: none;
  }
  .brand__name {
    font-family: "Montserrat", sans-serif;
    font-weight: 800;
    color: var(--ink);
    white-space: nowrap;
  }
  .brand__tagline {
    font-family: "Montserrat", sans-serif;
    font-weight: 500;
    white-space: nowrap;
  }

  /* front */
  .card--front .brand { left: 26px; top: 108px; width: 236px; }
  .card--front .brand__name { font-size: 17px; line-height: 20px; }
  .card--front .brand__tagline { font-size: 10px; color: var(--accent); margin-top: 2px; }

  .divider {
    position: absolute;
    left: 282px; top: 40px;
    width: 1px; height: 190px;
    background: var(--divider);
  }
  .details { position: absolute; left: 302px; top: 42px; width: 218px; }
  .details__name {
    font-family: "Montserrat", sans-serif;
    font-weight: 700; font-size: 23px; color: var(--ink);
    white-space: nowrap;
  }
  .details__role {
    font-family: "Montserrat", sans-serif;
    font-weight: 500; font-size: 14px; color: var(--accent);
    margin-bottom: 12px;
  }
  .contact { list-style: none; }
  .contact__item {
    display: flex; align-items: center; gap: 8px;
    font-size: 13px; color: var(--text-dark); line-height: 21px;
    white-space: nowrap;
  }
  .contact__icon {
    width: 17px; height: 17px; border-radius: 50%;
    background: var(--ink); flex: none;
    display: flex; align-items: center; justify-content: center;
  }
  .address { margin-top: 12px; font-size: 13px; color: var(--text-dark); line-height: 18px; }

  .services {
    position: absolute; left: 0; right: 0; bottom: 30px;
    text-align: center;
    font-size: 16px; color: var(--ink);
  }
  .services__sep {
    display: inline-block; width: 9px; height: 9px; border-radius: 50%;
    background: var(--accent); margin: 0 9px; vertical-align: middle;
  }

  /* back */
  .card--back .brand { left: 50%; top: 104px; transform: translateX(-50%); gap: 16px; }
  .card--back .brand__dot { width: 44px; height: 44px; background: var(--white); }
  .card--back .brand__name { color: var(--white); font-size: 26px; }
  .card--back .brand__tagline { color: var(--white); font-size: 13.5px; margin-top: 2px; }
  .social {
    position: absolute; left: 0; right: 0; bottom: 62px;
    display: flex; justify-content: center; align-items: center; gap: 10px;
    font-size: 13px;
  }
  .social__dot { width: 16px; height: 16px; border-radius: 50%; background: var(--white); }
</style>
</head>
<body>
  <section class="card card--front" aria-label="Card front">
    <div class="brand">
      <span class="brand__dot"></span>
      <div>
        <div class="brand__name">The Runner's Haven</div>
        <div class="brand__tagline">Sports medicine and athlete care</div>
      </div>
    </div>

    <span class="divider"></span>

    <div class="details">
      <div class="details__name">Daniel Brooks</div>
      <div class="details__role">Managing Director</div>
      <ul class="contact">
        <li class="contact__item">
          <span class="contact__icon">
            <svg width="10" height="10" viewBox="0 0 24 24"><path fill="#fff" d="M6.6 10.8a15 15 0 0 0 6.6 6.6l2.2-2.2c.3-.3.7-.4 1-.2 1.1.4 2.3.6 3.6.6.6 0 1 .4 1 1V20c0 .6-.4 1-1 1A17 17 0 0 1 3 4c0-.6.4-1 1-1h3.5c.6 0 1 .4 1 1 0 1.3.2 2.5.6 3.6.1.3 0 .7-.2 1z"/></svg>
          </span>041-555 208 317
        </li>
        <li class="contact__item">
          <span class="contact__icon">
            <svg width="10" height="10" viewBox="0 0 24 24"><rect x="2" y="5" width="20" height="14" rx="1.5" fill="#fff"/><path d="M3 6l9 7 9-7" fill="none" stroke="#0d2a6e" stroke-width="2"/></svg>
          </span>hello@runnershaven.com
        </li>
        <li class="contact__item">
          <span class="contact__icon">
            <svg width="11" height="11" viewBox="0 0 24 24" fill="none" stroke="#fff" stroke-width="2"><circle cx="12" cy="12" r="9"/><path d="M3 12h18M12 3c3 3 3 15 0 18M12 3c-3 3-3 15 0 18"/></svg>
          </span>www.runnershaven.com
        </li>
      </ul>
      <p class="address">18 Harbour Street, Suite 4<br>40210, Australia</p>
    </div>

    <p class="services">Coaching<span class="services__sep"></span>Dietetics<span class="services__sep"></span>Massage Therapy</p>
  </section>

  <section class="card card--back" aria-label="Card back">
    <div class="brand">
      <span class="brand__dot"></span>
      <div>
        <div class="brand__name">The Runner's Haven</div>
        <div class="brand__tagline">Sports medicine and athlete care</div>
      </div>
    </div>
    <div class="social">
      <span class="social__dot"></span>
      <span>RunnersHavenAU</span>
    </div>
  </section>
</body>
</html>
```